KELTO Robotics Engineering Design Team - Pull Up Banner Design

I need a pull-up banner design which I can use at trade shows and events to market our research and development group. We are specialist design engineers who have expertise in:
- Embedded Electronics and Circuit Design
- Rapid Functional Prototyping
- Sensor and Vision Systems
- Robotics Systems

Recent projects include:
- Robotic concrete sewer probes
- IoT wildlife tracking systems
- Robots for exploring wombat burrows
- Smart pest control technology

Target Market(s)

Potential clients who want us to design a project for them

Industry/Entity Type

Engineering Consulting

Colors

Designer to choose colors to be used in the design.

Requirements
Must have
• Look professional and have a high-tech feel to it

```html
<!DOCTYPE html>
<html lang="en">
<head>
<meta charset="utf-8">
<title>KELTO Robotics Engineering Design Team – Pull Up Banner</title>
<link href="https://fonts.googleapis.com/css2?family=Montserrat:wght@500;700;800&family=Roboto+Condensed:wght@400;500&display=swap" rel="stylesheet">
<style>
  :root {
    --brand-blue: #3a4c9f;
    --brand-red: #c3303a;
    --paper: #ffffff;
    --stage: #ffffff;
    --photo-sky: #b9d3ea;
    --photo-ground: #6f7a4e;
  }
  html, body {
    margin: 0;
    width: 1200px;
    height: 1200px;
    overflow: hidden;
    background: var(--stage);
  }
  .canvas {
    position: relative;
    width: 1200px;
    height: 1200px;
  }
  .banner {
    position: absolute;
    left: 370px;
    top: 40px;
    width: 640px;
    height: 1555px;
    transform: scale(0.72);
    transform-origin: top left;
    background: var(--paper);
    box-shadow: 0 6px 24px rgba(0,0,0,0.18);
    overflow: hidden;
    font-family: "Montserrat", sans-serif;
  }
  .banner-shapes {
    position: absolute;
    inset: 0;
    width: 640px;
    height: 1555px;
  }
  .wordmark {
    position: absolute;
    top: 78px;
    left: 0;
    width: 640px;
    text-align: center;
    font-family: "Montserrat", sans-serif;
    font-weight: 800;
    font-size: 94px;
    line-height: 110px;
    letter-spacing: 18px;
    text-indent: 18px;
    color: var(--brand-blue);
  }
  .tagline {
    position: absolute;
    left: 0;
    width: 640px;
    text-align: center;
    font-family: "Roboto Condensed", sans-serif;
    font-weight: 400;
    color: var(--brand-blue);
    margin: 0;
  }
  .tagline-primary { top: 184px; font-size: 24px; line-height: 28px; }
  .tagline-secondary { top: 214px; font-size: 24px; line-height: 28px; letter-spacing: 2px; }
  .header-url {
    position: absolute;
    top: 244px;
    left: 0;
    width: 640px;
    text-align: center;
    font-family: "Roboto Condensed", sans-serif;
    font-weight: 500;
    font-size: 32px;
    line-height: 36px;
    color: var(--brand-blue);
    margin: 0;
  }
  .content {
    position: absolute;
    left: 75px;
    right: 40px;
    color: var(--paper);
  }
  .section-title {
    margin: 0;
    font-weight: 800;
    font-size: 31px;
    line-height: 44px;
  }
  .section-rule {
    width: 32px;
    height: 4px;
    background: var(--paper);
    margin: 14px 0 0;
  }
  .feature-list {
    list-style: none;
    margin: 0;
    padding: 0;
    font-weight: 500;
    font-size: 24px;
    line-height: 30px;
  }
  .feature-list li {
    position: relative;
    padding-left: 35px;
    margin-bottom: 6.5px;
  }
  .feature-list li::before {
    content: "";
    position: absolute;
    left: 1px;
    top: 7px;
    width: 16px;
    height: 16px;
    background: var(--paper);
  }
  .expertise-title { top: 775px; }
  .expertise-rule { position: absolute; top: 922px; left: 75px; }
  .expertise-list { top: 942px; }
  .projects-title { top: 1130px; }
  .projects-rule { position: absolute; top: 1185px; left: 75px; }
  .projects-list { top: 1207px; }
  .footer-url {
    position: absolute;
    top: 1443px;
    left: 0;
    width: 640px;
    text-align: center;
    font-size: 32px;
    line-height: 40px;
    font-weight: 500;
    color: var(--paper);
    margin: 0;
  }
  .footer-url strong { font-weight: 700; }
</style>
</head>
<body>
<div class="canvas">
  <section class="banner">
    <svg class="banner-shapes" viewBox="0 0 640 1555" xmlns="http://www.w3.org/2000/svg" aria-hidden="false">
      <defs>
        <linearGradient id="team-photo-tone" x1="0" y1="0" x2="0" y2="1">
          <stop offset="0" stop-color="#c7dcef"/>
          <stop offset="0.35" stop-color="#a58d64"/>
          <stop offset="0.7" stop-color="#7c8a5a"/>
          <stop offset="1" stop-color="#5e6a42"/>
        </linearGradient>
      </defs>
      <polygon class="accent-line" points="0,289 640,352 640,360 0,297" fill="var(--brand-red)"/>
      <polygon class="band-blue-upper" points="0,297 640,358 640,420 0,302" fill="var(--brand-blue)"/>
      <polygon class="team-photo" role="img" aria-label="Photo of the engineering team in high-visibility vests deploying a sewer probe on a tripod beside utility vehicles" points="0,302 640,420 640,767 0,642" fill="url(#team-photo-tone)"/>
      <polygon class="band-blue-lower" points="0,642 640,767 640,772 0,708" fill="var(--brand-blue)"/>
      <polygon class="divider-white" points="0,708 640,772 640,778 0,714" fill="var(--paper)"/>
      <polygon class="panel-red" points="0,714 640,778 640,1422 0,1357" fill="var(--brand-red)"/>
      <polygon class="footer-blue" points="0,1357 640,1422 640,1555 0,1555" fill="var(--brand-blue)"/>
    </svg>

    <div class="wordmark">KELTO</div>
    <p class="tagline tagline-primary">ROBOTICS | AUTOMATION | MECHATRONICS</p>
    <p class="tagline tagline-secondary">PROTOTYPING | SENSING</p>
    <p class="header-url">keltolab.com</p>

    <h2 class="content section-title expertise-title">We Are Specialist<br>Design Engineers Who Have<br>Expertise In:</h2>
    <div class="section-rule expertise-rule"></div>
    <ul class="content feature-list expertise-list">
      <li>Embedded Electronics and<br>Circuit Design</li>
      <li>Rapid Functional Prototyping</li>
      <li>Sensor and Vision Systems</li>
      <li>Robotics Systems</li>
    </ul>

    <h2 class="content section-title projects-title">Recent Projects</h2>
    <div class="section-rule projects-rule"></div>
    <ul class="content feature-list projects-list">
      <li>Robotic concrete sewer probes</li>
      <li>IoT wildlife tracking systems</li>
      <li>Robots for exploring wombat burrows</li>
      <li>Smart pest control technology</li>
    </ul>

    <p class="footer-url">www.<strong>KeltoLab</strong>.com</p>
  </section>
</div>
</body>
</html>
```